Company letter head and business card for new Indian Pharmaceutical Export company.

We need a letterhead and business card design for an Indian Pharmaceutical Export company.

The letter head needs to contain the following information.
Verona Healthline Pvt. Ltd.
Office No 4837 Plot No 52, Kestrel Heights, RT Lane, 400517, Maharashtra, India.
Email: info@verona-healthline.example
Phone: +91-8213460592
CIN: U58213MH2025PTC719264
GSTIN: (This number is still pending, we will add later)

The business card needs to contain:
Address:
Verona Healthline Pvt. Ltd.
Office No 4837 Plot No52, Kestrel Heights, RT Lane, 400517, MH, India.
Email: tobias@verona-healthline.example
Phone: +49-17638421956
Name on card: Tobias Wendlinger
Position: Director

The design for the letter head and business card should be simple but trustworthy.
Please use only Green and blue, same as in the attached logo.

```html
<!DOCTYPE html>
<html lang="en">
<head>
<meta charset="utf-8">
<title>Verona Healthline Letterhead</title>
<link href="https://fonts.googleapis.com/css2?family=Open+Sans:wght@400;600;700&family=Roboto:wght@400&display=swap" rel="stylesheet">
<style>
  :root {
    --backdrop: #e4e4e4;
    --paper: #ffffff;
    --brand-blue: #1a5fa8;
    --brand-green: #7dc243;
    --ink: #1c1c1c;
    --ink-soft: #2a2a2a;
    --sig-tone: #d9dde6;
  }
  * { margin: 0; padding: 0; box-sizing: border-box; }
  html, body {
    width: 1174px; height: 1200px; overflow: hidden;
    background: var(--backdrop);
  }
  .letterhead {
    position: absolute; left: 136px; top: 16px;
    width: 902px; height: 1167px;
    background: var(--paper);
    box-shadow: 0 2px 8px rgba(0,0,0,0.18);
    font-family: "Open Sans", sans-serif;
    color: var(--ink);
  }
  .brand {
    position: absolute; left: 86px; top: 36px; width: 165px;
    display: flex; flex-direction: column; align-items: center;
  }
  .brand-mark { width: 156px; height: 156px; }
  .brand-name {
    margin-top: 10px; font-weight: 700; font-size: 19px;
    color: var(--brand-blue); white-space: nowrap;
  }
  .contact {
    position: absolute; right: 82px; top: 34px;
    text-align: right; font-family: "Roboto", sans-serif; font-style: normal;
    color: var(--ink-soft); font-size: 15.5px; line-height: 22px;
  }
  .contact-lines { margin-top: 13px; }
  .contact-line { display: flex; justify-content: flex-end; align-items: center; gap: 9px; }
  .contact-line svg { width: 13px; height: 13px; fill: var(--brand-blue); }
  .registry { margin-top: 12px; }
  .registry .label { color: var(--brand-green); }
  .recipient { position: absolute; left: 86px; top: 300px; }
  .recipient-name { font-size: 22.5px; font-weight: 600; line-height: 30px; }
  .recipient-role { font-size: 18px; line-height: 24px; }
  .date { position: absolute; right: 83px; top: 324px; font-size: 13px; }
  .body {
    position: absolute; left: 86px; top: 392px; width: 733px;
    font-size: 12.9px; line-height: 20.6px; text-align: justify;
  }
  .body p + p { margin-top: 20.6px; }
  .body p:last-child { text-align-last: justify; }
  .signature {
    position: absolute; left: 86px; top: 912px; width: 252px; height: 44px;
    background: linear-gradient(90deg, var(--sig-tone), #eef0f4);
    border-radius: 3px;
  }
  .signer { position: absolute; left: 86px; top: 992px; }
  .signer-name { font-size: 22.5px; font-weight: 600; line-height: 30px; }
  .signer-role { font-size: 18px; line-height: 24px; }
</style>
</head>
<body>
<main class="letterhead">
  <header>
    <div class="brand">
      <svg class="brand-mark" viewBox="0 0 150 150" aria-hidden="true">
        <circle cx="75" cy="75" r="68" fill="none" stroke="var(--brand-blue)" stroke-width="8"/>
      </svg>
      <div class="brand-name">Verona Healthline</div>
    </div>
    <address class="contact">
      <div>Verona Healthline Pvt. Ltd.</div>
      <div>Office No 4837 Plot No 52, Kestrel Heights,</div>
      <div>RT Lane, 400517, Maharashtra, India.</div>
      <div class="contact-lines">
        <div class="contact-line">+91-8213460592
          <svg viewBox="0 0 24 24"><path d="M6.6 10.8a15 15 0 0 0 6.6 6.6l2.2-2.2a1 1 0 0 1 1-.25 11.4 11.4 0 0 0 3.6.57 1 1 0 0 1 1 1V20a1 1 0 0 1-1 1A17 17 0 0 1 3 4a1 1 0 0 1 1-1h3.5a1 1 0 0 1 1 1c0 1.25.2 2.45.57 3.57a1 1 0 0 1-.25 1z"/></svg>
        </div>
        <div class="contact-line">info@verona-healthline.example
          <svg viewBox="0 0 24 24"><path d="M2 5h20v14H2z M2 5l10 8 10-8" fill="var(--brand-blue)" stroke="#fff" stroke-width="1.5"/></svg>
        </div>
        <div class="contact-line">www.verona-healthline.example
          <svg viewBox="0 0 24 24"><circle cx="12" cy="12" r="10"/><path d="M2 12h20M12 2c3 3 3 17 0 20M12 2c-3 3-3 17 0 20" fill="none" stroke="#fff" stroke-width="1.3"/></svg>
        </div>
      </div>
      <div class="registry">
        <div><span class="label">CIN:</span> U58213MH2025PTC719264</div>
        <div><span class="label">GSTIN:</span> (123456789)</div>
      </div>
    </address>
  </header>

  <section class="recipient">
    <div class="recipient-name">Dear .Mrs Leena Varma</div>
    <div class="recipient-role">Owner/ceo</div>
  </section>
  <div class="date">Date: 17-March-2025</div>

  <section class="body">
    <p>Lorem ipsum dolor sit amet, consectetur adipiscing elit. Mauris imperdiet ultricies nisi at varius. Ut euismod molestie lorem id maximus. Interdum et malesuada fames ac ante ipsum primis in faucibus. Sed sed enim urna. Mauris non elit quis nulla tincidunt maximus in a quam. Maecenas quis tellus ut eros auctor rhoncus non sed dui. Pellentesque habitant morbi tristique senectus et netus et malesuada fames ac turpis egestas. Aliquam in vulputate sapien. Donec eu eros congue, ultricies justo vel, rhoncus augue. Aenean et neque aliquet, fermentum sapien et, convallis velit.</p>
    <p>Sed imperdiet vehicula ligula. Proin sodales faucibus tortor sit amet fermentum. Donec varius massa vitae porta pharetra. Curabitur nec velit id ex pharetra ornare nec vel orci. Nam tristique diam sed ligula vehicula bibendum. Curabitur et libero lacinia sapien vehicula euismod non non tellus. Nulla facilisi.</p>
    <p>Nunc semper nisl eget dolor tempus tincidunt. Orci varius natoque penatibus et magnis dis parturient montes, nascetur ridiculus mus. Mauris at tristique quam, sed accumsan risus. Proin odio libero, dignissim a neque vitae, sodales tempor nisl. Nunc venenatis placerat vestibulum. Curabitur lacinia erat at malesuada tincidunt. Nulla commodo lobortis purus, in volutpat ex consectetur ut. Phasellus quis mi mi. Quisque mollis pharetra varius.</p>
    <p>Cras sed tortor faucibus, pellentesque lacus at, faucibus lacus. Sed ac lobortis diam. Duis eget sapien consequat quam scelerisque egestas in sit amet nunc. Praesent posuere, mi eu pulvinar vestibulum, mauris mi laoreet dui, ut lacinia neque elit sit amet metus. Donec gravida nisl ac sapien volutpat tristique. Duis porta enim eu leo faucibus, ac iaculis nibh venenatis. Cras non tincidunt libero. Etiam ligula elit, pulvinar ac massa ut, dapibus tincidunt lacus.</p>
    <p>Vivamus vel vehicula erat, vitae suscipit erat. Nullam lacinia, sem ac euismod cursus, justo nisi ultrices nunc, sed mollis eros diam quis lectus. In scelerisque aliquet dui. Morbi urna nunc, vestibulum eu ullamcorper a, tincidunt a nulla.</p>
  </section>

  <div class="signature" role="img" aria-label="Handwritten signature of the sender"></div>
  <section class="signer">
    <div class="signer-name">Mrs Leena Varma</div>
    <div class="signer-role">Owner/ceo</div>
  </section>
</main>
</body>
</html>
```